Support People to improve their image and well-being by provided personalised advise

We need a design for business cards that could be used for production on plato press. We build a new business in our region for advising mostly women (also men though) on style embracing several aspects including fashion, style, self-confidence and ultimately your internal and external image. The business card should be "classy", "french-style". The business is located in the french -speaking part of Switzerland, close to France. The name of the company is Velo Grace

Target Market(s)

Service fees won't be cheap (medium to premium) thus we target mid-class to upper-class women (1st target) and men (2nd target)

Industry/Entity Type

Life Coaching

Contact Information for Business Card

Conseil en Image

+41 79 418 62 07
morinetu@velo-grace.ch
linkvera.com/in/tu-moro-netia

Logo Text

Velo Grace

Colors

Designer to choose colors to be used in the design.

```html
<!DOCTYPE html>
<html lang="en">
<head>
<meta charset="utf-8">
<title>Velo Grace — Business Card</title>
<link rel="stylesheet" href="https://fonts.googleapis.com/css2?family=Lato:ital,wght@0,400;0,700;1,400&family=Pinyon+Script&display=swap">
<style>
  :root {
    --backdrop: #1e1e1e;
    --card-white: #fbfbfd;
    --plum-dark: #6e1a6c;
    --plum: #8a1f86;
    --magenta: #b01caf;
    --ink: #2a2a2a;
    --rule: #d9c3da;
    --white: #ffffff;
  }
  html, body {
    margin: 0;
    padding: 0;
    width: 1200px;
    height: 900px;
    overflow: hidden;
    background: var(--backdrop);
  }
  .stage {
    position: relative;
    width: 1200px;
    height: 900px;
  }
  .card {
    position: absolute;
    top: 306px;
    width: 439px;
    height: 271px;
    border-radius: 12px;
    box-shadow: 0 6px 10px rgba(0,0,0,0.55);
    overflow: hidden;
  }
  .card-front {
    left: 149px;
    background: var(--card-white);
  }
  .card-back {
    left: 608px;
    background:
      radial-gradient(ellipse 70% 60% at 80% 25%, rgba(190,30,190,0.55), transparent 70%),
      linear-gradient(135deg, var(--plum-dark) 0%, var(--magenta) 45%, var(--magenta) 65%, var(--plum-dark) 100%);
  }
  .brand-name {
    position: absolute;
    font-family: 'Lato', sans-serif;
    font-weight: 400;
    white-space: nowrap;
    letter-spacing: 1px;
    line-height: 1;
  }
  .card-front .brand-name {
    right: 18px;
    top: 58px;
    font-size: 36px;
    color: var(--plum);
  }
  .card-back .brand-name {
    left: 0;
    right: 0;
    top: 112px;
    text-align: center;
    font-size: 46px;
    color: var(--white);
  }
  .person-name {
    position: absolute;
    left: 22px;
    top: 140px;
    font-family: 'Pinyon Script', cursive;
    font-size: 36px;
    line-height: 1.2;
    color: var(--plum-dark);
    white-space: nowrap;
  }
  .role-line {
    position: absolute;
    left: 23px;
    top: 185px;
    width: 393px;
    display: flex;
    align-items: center;
    gap: 4px;
    font-family: 'Lato', sans-serif;
    font-size: 12px;
    color: var(--ink);
  }
  .role-line::after {
    content: "";
    flex: 1;
    height: 1px;
    background: var(--rule);
  }
  .contact-list {
    position: absolute;
    left: 24px;
    top: 213px;
    margin: 0;
    padding: 0;
    list-style: none;
    font-family: 'Lato', sans-serif;
    font-size: 12.5px;
    line-height: 17px;
    color: var(--ink);
  }
  .contact-list li {
    display: flex;
    align-items: center;
    gap: 3px;
  }
  .contact-icon {
    width: 11px;
    height: 11px;
    fill: var(--plum);
  }
  .social-link {
    position: absolute;
    right: 21px;
    top: 227px;
    display: flex;
    align-items: center;
    gap: 3px;
    font-family: 'Lato', sans-serif;
    font-style: italic;
    font-size: 12.5px;
    color: var(--ink);
  }
  .social-dot {
    width: 17px;
    height: 17px;
    border-radius: 50%;
    background: var(--plum);
  }
</style>
</head>
<body>
<main class="stage">
  <section class="card card-front" aria-label="Business card front">
    <div class="brand-name">Velo Grace</div>
    <div class="person-name">Elian Marchetti</div>
    <div class="role-line"><span>Managing Director</span></div>
    <ul class="contact-list">
      <li>
        <svg class="contact-icon" viewBox="0 0 24 24" aria-hidden="true"><path d="M3 9c0-3 4-5 9-5s9 2 9 5v2h-5V9.5c-1-.6-2.5-1-4-1s-3 .4-4 1V11H3z M6 13h12l2 7H4z"/></svg>
        <span>+41 79 418 62 07</span>
      </li>
      <li>
        <svg class="contact-icon" viewBox="0 0 24 24" aria-hidden="true"><path d="M2 6h20v12H2z M2 6l10 7 10-7"/></svg>
        <span>morinetu@velo-grace.ch</span>
      </li>
    </ul>
    <div class="social-link">
      <span>linkvera.com/in/tu-moro-netia</span>
      <span class="social-dot" aria-hidden="true"></span>
    </div>
  </section>

  <section class="card card-back" aria-label="Business card back">
    <div class="brand-name">Velo Grace</div>
  </section>
</main>
</body>
</html>
```